Falcrest security business card

Looking for a business card for my security company

Target Market(s)

Security

Industry/Entity Type

Security

Contact Information for Business Card

Name - Gil Marston. Title - General manager - direct 314 862.4490 website www. falcrestsecurityservices.example email - gil@ falcrestsecurityservices.example

Requirements
Must have
• Logo attached

```html
<!DOCTYPE html>
<html lang="en">
<head>
<meta charset="utf-8">
<title>Falcrest Security Services – Business Card</title>
<link rel="stylesheet" href="https://fonts.googleapis.com/css2?family=Jost:ital,wght@0,400;0,500;0,600;1,300&display=swap">
<style>
  :root {
    --backdrop: #fde09e;
    --card: #1a1a1a;
    --gold: #d8b46a;
    --gold-soft: rgba(216, 180, 106, 0.18);
  }
  * { box-sizing: border-box; margin: 0; padding: 0; }
  html, body {
    width: 1200px;
    height: 2400px;
    overflow: hidden;
    background: var(--backdrop);
  }
  .canvas {
    position: relative;
    width: 1200px;
    height: 2400px;
    font-family: "Jost", sans-serif;
    color: var(--gold);
  }
  .card {
    position: absolute;
    left: 124px;
    width: 952px;
    height: 615px;
    background: var(--card);
    overflow: hidden;
  }
  .card--front { top: 53px; }
  .card--back { top: 831px; }

  .card__artwork {
    position: absolute;
    left: 463px;
    top: 243px;
    right: 0;
    bottom: 0;
    background: radial-gradient(ellipse at 55% 45%, var(--gold-soft) 0%, rgba(216,180,106,0.06) 55%, transparent 80%);
  }

  .holder { position: absolute; left: 37px; top: 98px; }
  .holder__name {
    font-weight: 600;
    font-size: 62px;
    line-height: 1;
    letter-spacing: -0.5px;
  }
  .holder__title {
    font-weight: 300;
    font-style: italic;
    font-size: 31px;
    line-height: 1.1;
    margin-top: -2px;
    margin-left: 2px;
  }

  .wordmark {
    position: absolute;
    display: flex;
    align-items: center;
    gap: 12px;
    font-weight: 600;
    font-size: 46px;
    line-height: 1;
    letter-spacing: 1px;
    text-transform: uppercase;
  }
  .wordmark__square {
    width: 20px;
    height: 20px;
    background: var(--gold);
  }
  .card--front .wordmark { right: 70px; top: 98px; }
  .card--back .wordmark { left: 56px; top: 86px; }

  .contact {
    position: absolute;
    left: 38px;
    top: 452px;
    list-style: none;
    font-weight: 500;
    font-size: 24px;
    line-height: 35px;
  }
  .card__web {
    position: absolute;
    left: 56px;
    top: 551px;
    font-weight: 500;
    font-size: 26px;
    line-height: 1.2;
  }
</style>
</head>
<body>
<main class="canvas">
  <section class="card card--front" aria-label="Business card front">
    <div class="card__artwork" role="img" aria-label="Gold line drawing of a leaping big cat"></div>
    <header class="holder">
      <h1 class="holder__name">Gil Marston</h1>
      <p class="holder__title">General manager</p>
    </header>
    <div class="wordmark"><span class="wordmark__square"></span><span>Falcrest</span></div>
    <ul class="contact">
      <li>phone: 314 862.4490</li>
      <li>email: gil@falcrestsecurityservices.example</li>
      <li>www.falcrestsecurityservices.example</li>
    </ul>
  </section>

  <section class="card card--back" aria-label="Business card back">
    <div class="card__artwork" role="img" aria-label="Gold line drawing of a leaping big cat"></div>
    <div class="wordmark"><span class="wordmark__square"></span><span>Falcrest</span></div>
    <p class="card__web">www.falcrestsecurityservices.example</p>
  </section>
</main>
</body>
</html>
```